New Banner Ad Design Project

I would like to purchase a customized version of a design you have previously submitted - https://www.plavotrix.example/design/58302917

We need a banner ad (3ft x 5ft) design for our real estate sales company. We assist people with buying and selling homes! I would like a nice modern design but not to wordy or crowded.

```html
<!DOCTYPE html>
<html lang="en">
<head>
<meta charset="utf-8">
<title>Harlow Real Estate Team – Banner</title>
<link rel="stylesheet" href="https://fonts.googleapis.com/css2?family=Josefin+Sans:wght@600&family=Open+Sans:ital,wght@1,700&family=Roboto+Condensed:wght@500&display=swap">
<style>
  :root {
    --stage: #e4e4e4;
    --brand-red: #b5121b;
    --ink: #1a1a1a;
    --paper: #ffffff;
    --sky: #8fb6dc;
    --lawn: #4f8a2c;
    --sign: #d9d9d9;
  }
  html, body {
    margin: 0;
    width: 1200px;
    height: 726px;
    overflow: hidden;
    background: var(--stage);
  }
  .banner {
    position: absolute;
    left: 114px;
    top: 18px;
    width: 972px;
    height: 690px;
    display: block;
  }
  .team-name { font-family: "Josefin Sans", sans-serif; font-weight: 600; fill: var(--ink); }
  .tagline { font-family: "Open Sans", sans-serif; font-style: italic; font-weight: 700; font-size: 34px; }
  .tagline .accent { fill: var(--brand-red); }
  .tagline .plain { fill: var(--ink); }
  .contact { font-family: "Roboto Condensed", sans-serif; font-weight: 500; font-size: 13.5px; fill: var(--ink); }
  .web-address { font-family: "Roboto Condensed", sans-serif; font-weight: 500; font-size: 15px; fill: var(--paper); }
  .partner-name { font-family: "Roboto Condensed", sans-serif; font-weight: 500; font-size: 8px; fill: var(--brand-red); }
</style>
</head>
<body>
<svg class="banner" viewBox="0 0 652 463" xmlns="http://www.w3.org/2000/svg">
  <defs>
    <linearGradient id="house-photo-tone" x1="0" y1="0" x2="0" y2="1">
      <stop offset="0" stop-color="var(--sky)"/>
      <stop offset="0.45" stop-color="#7d8a96"/>
      <stop offset="0.7" stop-color="var(--lawn)"/>
      <stop offset="1" stop-color="#6f8f50"/>
    </linearGradient>
  </defs>

  <g class="house-photo" role="img" aria-label="Photo of a stone two-storey house with a grey roof, green lawn and curving driveway">
    <rect x="0" y="0" width="300" height="463" fill="url(#house-photo-tone)"/>
  </g>

  <polygon class="stripe-gap" points="180,0 192,0 222,270 212,272" fill="var(--paper)"/>
  <polygon class="stripe-red-thin" points="133,0 180,0 212,272 190,274" fill="var(--brand-red)"/>
  <polygon class="stripe-red-main" points="192,0 236,0 281,414 652,414 652,463 243,463" fill="var(--brand-red)"/>
  <polygon class="stripe-black" points="174,88 212,82 240,370 210,374" fill="var(--ink)"/>
  <polygon class="content-panel" points="236,0 652,0 652,414 281,414" fill="var(--paper)"/>

  <g class="partner-mark">
    <rect x="24" y="9" width="13" height="13" fill="var(--brand-red)"/>
    <text class="partner-name" x="41" y="15">Ridgeway Realty</text>
    <text class="partner-name" x="41" y="24">Partners</text>
  </g>

  <g class="team-logo">
    <text class="team-name" x="298" y="46" font-size="28">The</text>
    <text class="team-name" x="300" y="94" font-size="54" letter-spacing="4">HARLOW</text>
    <text class="team-name" x="304" y="117" font-size="17" letter-spacing="2.5">REAL ESTATE TEAM</text>
  </g>

  <text class="tagline" x="307" y="205"><tspan class="accent">Home</tspan> <tspan class="plain">Buying</tspan></text>
  <text class="tagline" x="440" y="250"><tspan class="accent">Made</tspan> <tspan class="plain">Easy</tspan></text>

  <g class="sale-sign" role="img" aria-label="Illustration of a white post with a hanging red For Sale sign">
    <rect x="328" y="300" width="96" height="112" fill="var(--sign)"/>
  </g>

  <g class="contact-phone">
    <rect x="460" y="324" width="13" height="13" rx="2" fill="var(--brand-red)"/>
    <path d="M464 327 q-1.5 3.5 1.5 7 l1.6-1.2 -1.5-2 q-0.6-1.2 0-2.4 l-0.6-1.6z" fill="var(--paper)"/>
    <text class="contact" x="482" y="336">(555)010-2014</text>
  </g>
  <g class="contact-email">
    <rect x="460" y="353" width="13" height="9" fill="none" stroke="var(--brand-red)" stroke-width="1.2"/>
    <path d="M460 353 l6.5 5 6.5-5" fill="none" stroke="var(--brand-red)" stroke-width="1.2"/>
    <text class="contact" x="482" y="362">info@harlowteamre.example</text>
  </g>

  <g class="contact-web">
    <circle cx="394" cy="439" r="7" fill="none" stroke="var(--paper)" stroke-width="1.2"/>
    <ellipse cx="394" cy="439" rx="3" ry="7" fill="none" stroke="var(--paper)" stroke-width="1"/>
    <line x1="387" y1="439" x2="401" y2="439" stroke="var(--paper)" stroke-width="1"/>
    <text class="web-address" x="413" y="444">www.harlowteamre.example</text>
  </g>
</svg>
</body>
</html>
```